BRIGHTWELL PROPERTY CHECKS Business card, please make it match the flyer.
Dana Pelworth
Dana@brightwellpropertychecksfl.example
555-218-7604 office
www.BrightwellPropertyChecks.example

Contact Information for Business Card

OUR LOGO

```html
<!DOCTYPE html>
<html lang="en">
<head>
<meta charset="utf-8">
<title>Brightwell Property Checks – Business Card</title>
<link href="https://fonts.googleapis.com/css2?family=Open+Sans:wght@400;600;700&display=swap" rel="stylesheet">
<style>
  :root {
    --stage: #262626;
    --card-front: #2b2b2d;
    --card-back: #1f1f24;
    --edge-red: #c8151c;
    --accent-red: #ee1c25;
    --accent-blue: #1565c8;
    --text-light: #f2f2f2;
    --brand-light: #ffffff;
  }
  * { box-sizing: border-box; margin: 0; padding: 0; }
  html, body {
    width: 1200px; height: 780px; overflow: hidden;
    background: var(--stage);
    font-family: "Open Sans", Arial, sans-serif;
  }
  .stage {
    width: 1200px; height: 780px;
    display: flex; align-items: center; justify-content: center; gap: 40px;
  }
  .card {
    position: relative;
    width: 540px; height: 310px;
    border-radius: 20px;
    border: 3px solid var(--edge-red);
    box-shadow: 0 14px 30px rgba(0,0,0,.55);
    overflow: hidden;
  }
  .card--front { background: var(--card-front); display: flex; align-items: center; justify-content: center; }
  .card--back { background: var(--card-back); }

  .brand {
    display: flex; align-items: center; gap: 12px;
    color: var(--brand-light);
    font-weight: 700;
    letter-spacing: .5px;
    line-height: 1.1;
  }
  .brand__mark { width: 16px; height: 16px; background: var(--accent-red); flex: none; }
  .card--front .brand { font-size: 26px; }
  .card--back .brand { position: absolute; left: 34px; top: 44px; font-size: 17px; width: 230px; }

  .brand-watermark {
    position: absolute; right: 20px; top: 70px; width: 250px;
    color: #ffffff; opacity: .07;
    font-weight: 700; font-size: 34px; line-height: 1.05;
    text-align: center;
  }

  .holder-name {
    position: absolute; right: 48px; top: 64px;
    font-size: 30px; font-weight: 700; letter-spacing: .3px;
  }
  .holder-name__first { color: var(--accent-red); }
  .holder-name__last { color: var(--accent-blue); }
  .holder-bar {
    position: absolute; right: 18px; top: 58px;
    width: 16px; height: 44px; background: var(--accent-red);
  }

  .contact {
    position: absolute; left: 34px; bottom: 26px;
    color: var(--text-light); font-size: 14.5px; line-height: 1.35;
  }
  .contact__address { margin-bottom: 12px; }
  .contact__row { display: flex; align-items: center; gap: 9px; }
  .contact__icon { width: 14px; height: 14px; flex: none; fill: var(--accent-red); }
</style>
</head>
<body>
<main class="stage">

  <section class="card card--front" aria-label="Business card front">
    <div class="brand"><span class="brand__mark"></span>BRIGHTWELL PROPERTY CHECKS</div>
  </section>

  <section class="card card--back" aria-label="Business card back">
    <div class="brand-watermark" aria-hidden="true">BRIGHTWELL PROPERTY CHECKS</div>
    <div class="brand"><span class="brand__mark"></span>BRIGHTWELL PROPERTY CHECKS</div>

    <span class="holder-bar"></span>
    <h1 class="holder-name"><span class="holder-name__first">Dana</span> <span class="holder-name__last">Pelworth</span></h1>

    <address class="contact" style="font-style:normal">
      <p class="contact__address">418 Harlow Ave, Fenwick,<br>FL 30127</p>
      <p class="contact__row">
        <svg class="contact__icon" viewBox="0 0 24 24" aria-hidden="true"><path d="M6.6 10.8a15.1 15.1 0 0 0 6.6 6.6l2.2-2.2a1 1 0 0 1 1-.25 11.4 11.4 0 0 0 3.6.6 1 1 0 0 1 1 1V20a1 1 0 0 1-1 1A17 17 0 0 1 3 4a1 1 0 0 1 1-1h3.5a1 1 0 0 1 1 1c0 1.25.2 2.45.6 3.6a1 1 0 0 1-.25 1z"/></svg>
        555-218-7604 office
      </p>
      <p class="contact__row">
        <svg class="contact__icon" viewBox="0 0 24 24" aria-hidden="true"><path d="M12 2a10 10 0 1 0 0 20 10 10 0 0 0 0-20zm6.9 6h-3a15.6 15.6 0 0 0-1.4-3.6A8 8 0 0 1 18.9 8zM12 4c.8 1.2 1.5 2.5 1.9 4h-3.8c.4-1.4 1.1-2.8 1.9-4zM4.3 14a8 8 0 0 1 0-4h3.4a16 16 0 0 0 0 4zm.8 2h3a15.6 15.6 0 0 0 1.4 3.6A8 8 0 0 1 5.1 16zm3-8h-3a8 8 0 0 1 4.4-3.6A15.6 15.6 0 0 0 8.1 8zM12 20c-.8-1.2-1.5-2.5-1.9-4h3.8c-.4 1.4-1.1 2.8-1.9 4zm2.3-6H9.7a14.7 14.7 0 0 1 0-4h4.6a14.7 14.7 0 0 1 0 4zm.2 5.6a15.6 15.6 0 0 0 1.4-3.6h3a8 8 0 0 1-4.4 3.6zm1.8-5.6a16 16 0 0 0 0-4h3.4a8 8 0 0 1 0 4z"/></svg>
        www.BrightwellPropertyChecks.example
      </p>
      <p class="contact__row">
        <svg class="contact__icon" viewBox="0 0 24 24" aria-hidden="true"><path d="M3 5h18a1 1 0 0 1 1 1v12a1 1 0 0 1-1 1H3a1 1 0 0 1-1-1V6a1 1 0 0 1 1-1zm9 7.2L4.6 7H19.4zM4 8.6V17h16V8.6l-8 5.6z"/></svg>
        Dana@brightwellpropertychecksfl.example
      </p>
    </address>
  </section>

</main>
</body>
</html>
```